Garden Design Flier

I would like a PDF of this half page A4 flier in soft green tones with dark green leaves.

Target Market(s)

Home owners and real estate agents

Font styles to use
Serif
Other font styles liked:
• Papyrus

Colors
acd136
9bcb3c
cadf82
fefdec

Requirements
Must have
• Green tones
Nice to have
• Leaves, vines, lawns
Should not have
• Open to ideas, but classic style

```html
<!DOCTYPE html>
<html lang="en">
<head>
<meta charset="utf-8">
<title>Verdant Gardens – Flier</title>
<link rel="stylesheet" href="https://fonts.googleapis.com/css2?family=Lora:wght@400;600;700&display=swap">
<style>
  :root {
    --teal: #2fb8a5;
    --ink: #1d2b2a;
    --paper: #f7f7f7;
    --stage: #e9e7e3;
    --lawn-light: #7ccf3a;
    --lawn-dark: #2f6b24;
    --white: #ffffff;
  }
  html, body {
    margin: 0;
    width: 1200px;
    height: 1200px;
    overflow: hidden;
    background: var(--stage);
  }
  .canvas {
    width: 1200px;
    height: 1200px;
    display: flex;
    align-items: center;
    justify-content: center;
  }
  .flier {
    width: 1120px;
    height: 786px;
    display: block;
    box-shadow: 0 6px 18px rgba(0,0,0,.18);
  }
  .brand-name { font-family: "Lora", serif; font-weight: 600; fill: var(--teal); }
  .byline { font-family: "Lora", serif; font-weight: 400; fill: var(--ink); }
  .byline-name { font-weight: 700; }
  .tagline { font-family: "Lora", serif; font-weight: 700; fill: var(--teal); }
  .services { font-family: "Lora", serif; font-weight: 400; fill: var(--ink); }
  .contact { font-family: "Lora", serif; font-weight: 400; fill: var(--white); }
</style>
</head>
<body>
<main class="canvas">
  <svg class="flier" viewBox="0 0 1256 882" xmlns="http://www.w3.org/2000/svg">
    <defs>
      <linearGradient id="lawnTone" x1="0" y1="0" x2="1" y2="1">
        <stop offset="0" stop-color="var(--lawn-dark)"/>
        <stop offset="0.45" stop-color="#3f8a2c"/>
        <stop offset="0.7" stop-color="var(--lawn-light)"/>
        <stop offset="1" stop-color="#5fbf2e"/>
      </linearGradient>
    </defs>

    <rect class="paper" width="1256" height="882" fill="var(--paper)"/>

    <g class="hero-photo" role="img" aria-label="Photo of a landscaped front garden with clipped shrubs, a red flower border and a green lawn">
      <path d="M0 0 H1256 V165 C1060 270 820 305 620 295 C400 284 200 220 0 110 Z" fill="url(#lawnTone)"/>
    </g>

    <path class="hero-gap" d="M0 110 C200 220 400 284 620 295 C820 305 1060 270 1256 165 V185 C1060 282 820 315 620 308 C400 300 200 240 0 130 Z" fill="var(--white)"/>
    <path class="hero-swoosh" d="M0 118 C180 225 390 298 620 312 C850 325 1060 285 1220 210 C1070 300 860 338 620 332 C380 325 170 255 0 168 Z" fill="var(--teal)"/>

    <text class="brand-name" x="628" y="490" font-size="100" text-anchor="middle">Verdant Gardens</text>

    <text class="byline" x="628" y="597" font-size="28" text-anchor="middle"><tspan class="byline-name">by Liam Hartwell</tspan> Certificate 3. Horticulture. Coastal Institute</text>

    <path class="services-frame" d="M305 650 H98 V750 H1158 V650 H951" fill="none" stroke="var(--ink)" stroke-width="1.5"/>
    <text class="tagline" x="628" y="661" font-size="34" text-anchor="middle">Design Install Grow Tend Enjoy</text>
    <text class="services" x="628" y="699" font-size="19.5" text-anchor="middle">All your gardening and landscaping needs from design and installation to general maintenance</text>
    <text class="services" x="628" y="724" font-size="19.5" text-anchor="middle">Bespoke vegetable gardens and potager designs created to suit your site and requirements.</text>

    <path class="contact-band" fill="var(--teal)" d="M0 800 q11 -22 22 0 t22 0 t22 0 t22 0 t22 0 t22 0 t22 0 t22 0 t22 0 t22 0 t22 0 t22 0 t22 0 t22 0 t22 0 t22 0 t22 0 t22 0 t22 0 t22 0 t22 0 t22 0 t22 0 t22 0 t22 0 t22 0 t22 0 t22 0 t22 0 t22 0 t22 0 t22 0 t22 0 t22 0 t22 0 t22 0 t22 0 t22 0 t22 0 t22 0 t22 0 t22 0 t22 0 t22 0 t22 0 t22 0 t22 0 t22 0 t22 0 t22 0 t22 0 t22 0 t22 0 t22 0 t22 0 t22 0 t22 0 L1256 796 V882 H0 Z"/>

    <g class="contact-phone">
      <path d="M100 826 c-4 2 -6 8 -4 16 c2 8 6 13 10 14 l3 -4 l-5 -5 l-3 2 c-2 -3 -3 -8 -2 -11 l4 0 l0 -7 z" fill="var(--white)"/>
      <text class="contact" x="123" y="848" font-size="24">0400-182653</text>
    </g>
    <g class="contact-email">
      <rect x="419" y="832" width="28" height="17" fill="var(--white)"/>
      <path d="M419 832 L433 843 L447 832" fill="none" stroke="var(--teal)" stroke-width="2"/>
      <text class="contact" x="461" y="847" font-size="23">liam@verdantgardens.com.au</text>
    </g>
    <text class="contact" x="1166" y="848" font-size="24" text-anchor="end">ABN: 51902476318</text>
  </svg>
</main>
</body>
</html>
```